IT Product Event Invitations

We are requesting the design of two invitations for a series of technological events that will be held between the company Velto Grid and its partner in the Dominican Republic, Corvanel.
Both events represent the launch of the Velto Grid brand in the Dominican Republic.
The first event is an elegant dinner aimed at the banking sector of the Dominican Republic to showcase the "Ledgerwise Suite" software.
Event information:
- Descriptive text for the invitation: Corvanel y Velto Grid le invitan a descubrir cómo reducir costos, aumentar la automatización y mejorar la satisfacción de los clientes a través de una solución única para enfrentar los desafíos de la banca.
- Date: 25 de Septiembre
- Time: 7PM
- Location: El Miradero, Av. Tomás Herrandez 817
In the invitation, consider using the colors of the Velto Grid and Corvanel brands if possible. You can find the logos in the webpage
The second event is a wine tasting to present "Orbital Desk Platform" aimed at various industries.
Event information:
- Descriptive text for the invitation: Corvanel y Velto Grid le invitan a conocer una solución que le permitirá a toda su empresa brindar una experiencia de servicio a otro nivel.
- Date: 26 de Septiembre
- Time: 7PM
In the invitation, consider using the colors of the Velto Grid and Corvanel brands if possible. You can find the logos in the web page.
Both invitations must have a button for participant registration and that when you click on the image, it will direct you to a form.
Form for Ledgerwise Suite: https://signup.quilvane.example/events/a7Kq2Rm9Xw4Tz1Lp8Vb3Nc6Hd0Jf5Gs
Form for Orbital Desk Platform: https://signup.quilvane.example/events/b3Wd8Yt1Pq6Rn4Ks0Mz7Fc2Lx9Hv5Je

```html
<!DOCTYPE html>
<html lang="es">
<head>
<meta charset="utf-8">
<title>Invitaciones Corvanel y Velto Grid</title>
<link rel="stylesheet" href="https://fonts.googleapis.com/css2?family=Archivo:wght@400;500;700;800&display=swap">
<style>
  :root{
    --stage:#7accce;
    --navy:#172b4a;
    --charcoal:#2b2b2b;
    --peach:#f8d5a6;
    --blush:#efc3b3;
    --orange:#f29a3f;
    --red:#e8322a;
    --green:#5fd94f;
    --white:#ffffff;
    --ink:#1b1b1b;
  }
  *{box-sizing:border-box;margin:0;padding:0}
  html,body{width:1200px;height:872px;overflow:hidden}
  body{background:var(--stage);font-family:"Archivo",Arial,sans-serif;position:relative}
  .invite{position:absolute;top:139px;width:270px;height:594px;display:block;overflow:hidden;text-decoration:none;color:var(--ink);background:var(--body)}
  .invite--dinner{left:285px;--body:var(--navy);--band:var(--peach)}
  .invite--wine{left:645px;--body:var(--charcoal);--band:var(--blush)}
  .invite__art{position:absolute;inset:0}
  .brandbar{position:absolute;left:0;top:0;width:270px;height:48px;display:flex;align-items:center;justify-content:space-between;padding:0 14px 0 18px;background:var(--body)}
  .invite--wine .brandbar{background:#222}
  .brand{color:var(--white);font-weight:800;font-size:15px;letter-spacing:.2px;display:flex;align-items:center;gap:6px}
  .brand__dot{width:14px;height:14px;border-radius:50%;background:var(--red)}
  .intro{position:absolute;left:8px;right:8px;top:62px;text-align:center;font-size:8.1px;line-height:1.22}
  .intro strong{font-weight:500}
  .title{position:absolute;left:70px;width:160px;top:160px;text-align:center;color:var(--white)}
  .title h1{font-weight:800;font-size:17px;line-height:1.05;letter-spacing:.2px}
  .title .date{font-weight:700;font-size:10.5px;margin-top:4px}
  .title .venue{font-weight:700;font-size:10px;margin-top:2px}
  .title .addr{font-size:6.8px;font-weight:400}
  .rsvp{position:absolute;left:106px;top:515px;width:142px;height:49px;background:var(--green);border:2px solid var(--white);border-radius:8px 10px 40px 8px;display:flex;align-items:center;justify-content:center;font-weight:800;font-size:27px;color:var(--ink);letter-spacing:.5px}
</style>
</head>
<body>

<a class="invite invite--dinner" href="https://signup.quilvane.example/events/a7Kq2Rm9Xw4Tz1Lp8Vb3Nc6Hd0Jf5Gs">
  <svg class="invite__art" viewBox="0 0 270 594" width="270" height="594" aria-hidden="false">
    <defs>
      <linearGradient id="heat1" x1="0" x2="1"><stop offset="0" stop-color="#f29a3f"/><stop offset="1" stop-color="#e8322a"/></linearGradient>
      <linearGradient id="team1" x1="0" y1="0" x2="1" y2="1"><stop offset="0" stop-color="#0f3a5a"/><stop offset=".5" stop-color="#3aa89a"/><stop offset="1" stop-color="#1b3550"/></linearGradient>
      <linearGradient id="venue1" x1="0" y1="0" x2="1" y2="1"><stop offset="0" stop-color="#2f3a26"/><stop offset="1" stop-color="#5d6b3a"/></linearGradient>
      <linearGradient id="plate1" x1="0" y1="0" x2="1" y2="1"><stop offset="0" stop-color="#e9e6e1"/><stop offset="1" stop-color="#7a5a3c"/></linearGradient>
    </defs>
    <rect x="0" y="48" width="270" height="124" fill="var(--band)"/>
    <circle cx="251" cy="168" r="43" fill="#e8322a"/>
    <circle cx="15" cy="358" r="26" fill="#e8322a"/>
    <path d="M60 250 C100 215 200 200 270 230 L270 390 C220 420 140 445 90 430 C50 415 35 300 60 250 Z" fill="url(#team1)" stroke="#fff" stroke-width="1.6" role="img" aria-label="Foto de tres profesionales de negocios"/>
    <path d="M128 120 C70 150 60 230 82 270" fill="none" stroke="#f29a3f" stroke-width=".8" stroke-dasharray="3 2"/>
    <path d="M230 250 C260 270 275 300 270 330" fill="none" stroke="#5fd94f" stroke-width=".8" stroke-dasharray="3 2"/>
    <path d="M270 400 C220 440 150 460 95 455" fill="none" stroke="#5fd94f" stroke-width=".8" stroke-dasharray="3 2"/>
    <path d="M149 111 C190 110 230 160 228 200 C226 240 170 275 125 270 C85 266 68 230 72 190 C76 140 110 112 149 111 Z" fill="url(#heat1)" stroke="#fff" stroke-width="1.4"/>
    <path d="M190 292 L194 304 L206 308 L194 312 L190 324 L186 312 L174 308 L186 304 Z" fill="#5fd94f"/>
    <path d="M13 420 C15 380 60 378 85 395 C110 412 105 470 80 478 C50 486 11 465 13 420 Z" fill="url(#venue1)" stroke="#fff" stroke-width="1.4" role="img" aria-label="Foto de la terraza del restaurante"/>
    <path d="M36 520 C38 480 80 468 110 490 C130 505 125 545 100 552 C70 560 35 555 36 520 Z" fill="url(#plate1)" stroke="#fff" stroke-width="1.4" role="img" aria-label="Foto de un plato gourmet"/>
    <g fill="#f29a3f"><circle cx="13" cy="178" r="3"/><circle cx="245" cy="222" r="3"/><circle cx="10" cy="302" r="3"/></g>
    <g fill="#e8322a"><circle cx="10" cy="196" r="3"/><circle cx="49" cy="240" r="3"/><circle cx="27" cy="272" r="3"/><circle cx="30" cy="327" r="3"/><circle cx="228" cy="497" r="3"/></g>
  </svg>
  <div class="brandbar"><span class="brand"><span class="brand__dot"></span>Corvanel</span><span class="brand">Velto Grid</span></div>
  <p class="intro"><strong>Corvanel y Velto Grid<br>le invitan a descubrir cómo reducir costos,<br>aumentar la automatización</strong> y mejorar la satisfacción de los clientes a través de una solución única para enfrentar los desafíos de la banca.</p>
  <div class="title">
    <h1>INVITACIÓN<br>A LA CENA</h1>
    <p class="date">25 de Septiembre, 7pm</p>
    <p class="venue">El Miradero,</p>
    <p class="addr">Av. Tomás Herrandez 817</p>
  </div>
  <span class="rsvp">RSVP</span>
</a>

<a class="invite invite--wine" href="https://signup.quilvane.example/events/b3Wd8Yt1Pq6Rn4Ks0Mz7Fc2Lx9Hv5Je">
  <svg class="invite__art" viewBox="0 0 270 594" width="270" height="594">
    <defs>
      <linearGradient id="heat2" x1="0" x2="1"><stop offset="0" stop-color="#f29a3f"/><stop offset="1" stop-color="#e8322a"/></linearGradient>
      <linearGradient id="team2" x1="0" y1="0" x2="1" y2="1"><stop offset="0" stop-color="#0f3a5a"/><stop offset=".5" stop-color="#3aa89a"/><stop offset="1" stop-color="#1b3550"/></linearGradient>
      <linearGradient id="wine2" x1="0" y1="0" x2="1" y2="1"><stop offset="0" stop-color="#4a2414"/><stop offset="1" stop-color="#c9782e"/></linearGradient>
      <linearGradient id="cellar2" x1="0" y1="0" x2="1" y2="1"><stop offset="0" stop-color="#1c1a18"/><stop offset="1" stop-color="#6b5a45"/></linearGradient>
    </defs>
    <rect x="0" y="48" width="270" height="124" fill="var(--band)"/>
    <circle cx="251" cy="168" r="43" fill="#e8322a"/>
    <circle cx="15" cy="358" r="26" fill="#e8322a"/>
    <path d="M60 250 C100 215 200 200 270 230 L270 390 C220 420 140 445 90 430 C50 415 35 300 60 250 Z" fill="url(#team2)" stroke="#fff" stroke-width="1.6" role="img" aria-label="Foto de tres profesionales de negocios"/>
    <path d="M128 120 C70 150 60 230 82 270" fill="none" stroke="#f29a3f" stroke-width=".8" stroke-dasharray="3 2"/>
    <path d="M230 250 C260 270 275 300 270 330" fill="none" stroke="#5fd94f" stroke-width=".8" stroke-dasharray="3 2"/>
    <path d="M270 400 C220 440 150 460 95 455" fill="none" stroke="#5fd94f" stroke-width=".8" stroke-dasharray="3 2"/>
    <path d="M149 111 C190 110 230 160 228 200 C226 240 170 275 125 270 C85 266 68 230 72 190 C76 140 110 112 149 111 Z" fill="url(#heat2)" stroke="#fff" stroke-width="1.4"/>
    <path d="M194 292 L198 304 L210 308 L198 312 L194 324 L190 312 L178 308 L190 304 Z" fill="#5fd94f"/>
    <path d="M13 420 C15 380 60 378 85 395 C110 412 105 470 80 478 C50 486 11 465 13 420 Z" fill="url(#wine2)" stroke="#fff" stroke-width="1.4" role="img" aria-label="Foto de vino servido en copa"/>
    <path d="M36 520 C38 480 80 468 110 490 C130 505 125 545 100 552 C70 560 35 555 36 520 Z" fill="url(#cellar2)" stroke="#fff" stroke-width="1.4" role="img" aria-label="Foto de una cava de botellas"/>
    <g fill="#f29a3f"><circle cx="18" cy="111" r="3"/><circle cx="250" cy="212" r="3"/><circle cx="15" cy="292" r="3"/></g>
    <g fill="#e8322a"><circle cx="15" cy="138" r="3"/><circle cx="55" cy="178" r="3"/><circle cx="33" cy="216" r="3"/><circle cx="36" cy="316" r="3"/><circle cx="242" cy="492" r="3"/></g>
    <g fill="#5fd94f"><circle cx="204" cy="126" r="3"/><circle cx="46" cy="242" r="3"/><circle cx="142" cy="478" r="3"/><circle cx="23" cy="514" r="3"/></g>
  </svg>
  <div class="brandbar"><span class="brand"><span class="brand__dot"></span>Corvanel</span><span class="brand">Velto Grid</span></div>
  <p class="intro" style="top:63px;font-size:8.4px;font-weight:500">Corvanel y Velto Grid<br>le invitan a conocer una solución<br>que le permitirá a toda su empresa brindar<br>una experiencia de servicio a otro nivel.</p>
  <div class="title" style="top:150px">
    <h1>DEGUSTACIÓN<br>DE VINOS</h1>
    <p class="date">26 de Septiembre, 7pm</p>
    <p class="venue">El Miradero,</p>
    <p class="addr">Av. Tomás Herrandez 817</p>
  </div>
  <span class="rsvp">RSVP</span>
</a>

</body>
</html>
```